Stationery Design Project for Kwok Sing Resources

Kwok Sing Resources is a trading company originating in Hong Kong. We need full package of stationery designs that will include:

Business cards
Folder
Letter head
Envelopes large and small
Invoice
Packing list
Purchase order
Thank you card

All files shall be delivered in open source where the modification could be done.

```html
<!DOCTYPE html>
<html lang="en">
<head>
<meta charset="utf-8">
<title>Kwok Sing Resources — Business Card</title>
<link href="https://fonts.googleapis.com/css2?family=Open+Sans:wght@400;700&display=swap" rel="stylesheet">
<style>
  :root{
    --brand-green:#10904a;
    --deep-green:#0e7a3e;
    --ink:#1c1c1c;
    --muted:#8a8a8a;
    --paper:#ffffff;
    --backdrop:#e9e7e2;
  }
  *{box-sizing:border-box;margin:0;padding:0}
  html,body{width:1200px;height:900px;overflow:hidden}
  body{
    background:var(--backdrop);
    font-family:"Open Sans",Arial,sans-serif;
    position:relative;
  }
  .card{
    position:absolute;
    left:310px;
    width:580px;
    height:330px;
    border-radius:4px;
    box-shadow:0 6px 18px rgba(0,0,0,.18);
  }
  .card--back{top:60px;background:var(--brand-green);display:flex;align-items:center;justify-content:center}
  .card--front{top:470px;background:var(--paper);display:flex}

  .wordmark{display:flex;align-items:center;gap:12px}
  .wordmark__dot{width:16px;height:16px;border-radius:50%}
  .wordmark__name{font-weight:700;font-size:30px;line-height:1.05;letter-spacing:.5px;text-transform:uppercase}
  .card--back .wordmark__dot{background:var(--paper)}
  .card--back .wordmark__name{color:var(--paper)}
  .card--front .wordmark__dot{background:var(--brand-green)}
  .card--front .wordmark__name{color:var(--brand-green)}

  .card__brand{width:300px;display:flex;align-items:center;justify-content:center;padding-left:20px}
  .card__divider{width:1px;background:#9a9a9a;margin:50px 0}
  .card__details{flex:1;padding:50px 24px 0 26px}
  .person__name{color:var(--deep-green);font-weight:700;font-size:16px}
  .person__role{color:var(--ink);font-size:13px;margin-bottom:30px}
  .contact{list-style:none}
  .contact__item{display:flex;align-items:flex-start;gap:12px;font-size:13.5px;color:var(--ink);line-height:1.3;margin-bottom:7px}
  .contact__icon{flex:none;width:17px;height:17px;border-radius:50%;background:var(--brand-green);display:flex;align-items:center;justify-content:center}
  .contact__icon svg{width:11px;height:11px}
</style>
</head>
<body>
  <section class="card card--back">
    <div class="wordmark">
      <span class="wordmark__dot"></span>
      <span class="wordmark__name">Kwok Sing<br>Resources</span>
    </div>
  </section>

  <section class="card card--front">
    <div class="card__brand">
      <div class="wordmark">
        <span class="wordmark__dot"></span>
        <span class="wordmark__name">Kwok Sing<br>Resources</span>
      </div>
    </div>
    <div class="card__divider"></div>
    <div class="card__details">
      <p class="person__name">Daniel Weller</p>
      <p class="person__role">Director</p>
      <ul class="contact">
        <li class="contact__item">
          <span class="contact__icon"><svg viewBox="0 0 12 12"><path d="M6 1a3.5 3.5 0 0 0-3.5 3.5C2.5 7.5 6 11 6 11s3.5-3.5 3.5-6.5A3.5 3.5 0 0 0 6 1zm0 5a1.5 1.5 0 1 1 0-3 1.5 1.5 0 0 1 0 3z" fill="#fff"/></svg></span>
          <span>Harbour Road 28, Unit 7B<br>Wan Chai, Hong Kong</span>
        </li>
        <li class="contact__item">
          <span class="contact__icon"><svg viewBox="0 0 12 12"><path d="M3 1.5l2 2-1 1.2a6 6 0 0 0 3.3 3.3l1.2-1 2 2-1.2 1.5C5.5 10.5 1.5 6.5 1.5 2.7z" fill="#fff"/></svg></span>
          <span>852-555-0142</span>
        </li>
        <li class="contact__item">
          <span class="contact__icon"><svg viewBox="0 0 12 12"><rect x="2" y="4" width="8" height="6" rx="1" fill="#fff"/><rect x="3.5" y="1.5" width="5" height="3" fill="#fff"/></svg></span>
          <span>852-555-0149</span>
        </li>
        <li class="contact__item">
          <span class="contact__icon"><svg viewBox="0 0 12 12"><rect x="1.5" y="3" width="9" height="6" rx="1" fill="none" stroke="#fff" stroke-width="1.2"/><path d="M1.8 3.4L6 6.5l4.2-3.1" fill="none" stroke="#fff" stroke-width="1.2"/></svg></span>
          <span>daniel@kwoksing.com</span>
        </li>
        <li class="contact__item">
          <span class="contact__icon"><svg viewBox="0 0 12 12"><circle cx="6" cy="6" r="4.3" fill="none" stroke="#fff" stroke-width="1.1"/><path d="M1.7 6h8.6M6 1.7c-2 2.4-2 6.2 0 8.6M6 1.7c2 2.4 2 6.2 0 8.6" fill="none" stroke="#fff" stroke-width="1"/></svg></span>
          <span>www.kwoksing.com</span>
        </li>
      </ul>
    </div>
  </section>
</body>
</html>
```